FenderPals Personal Injury Lawyers Website (Wordpress)

We need a brand new website for our firm's new rebranding. The name of the website is www.fenderpals-example.com. Our new brand will be a group of personal injury lawyers focused on representing only victims in car wrecks. We will be distinguishing ourselves from other law firms due to the fact that other law firms represent clients involving all forms of personal injury. We will only focus on car wrecks and this needs to be reflected on the website.

I have attached the new firm logo and stationary to show the designers the kind of look we are going for in the new website. It needs to be clean, pure, and show the potential clients that we only do one thing and we do it well. That thing is car wrecks.

Some examples of websites that we like are the following:
www.qvt-example.lu - nice interface and colors. nice navigation, we really like the biography pages for the individuals attorneys
www.morvantlegal-example.com - good layout, good navigation
www.pelliardwoss-example.com - navigation bar follows the user whether the user goes up or down

We would like five separate pages -- (1) Home, (2) Client Resources, (3) Expertise / Car Wrecks, (4) Contact Us, (5) News

The Home page will be used for driving traffic and should have a call to action on the right at the top stating that we will send an ebook to anyone who gives their contact information. The ebook will explain how car wrecks work. This should also have room for youtube videos which will be added later.

The client resources will include blogs, books, and information for potential clients. It should be presented in a well developed manner which is both appealing to potential and current clients.

The expertise page will show that we only focus on car wrecks. This needs to be a recurrent theme throughout the entire website. This page will focus on car wrecks and the different aspects including damages, insurance, and investigation.

The Contact Us page will show a google map to our address and phone number. Please use generic information and we will fill in the gaps upon the selection.

News: the news page will show different articles related to past and present cases and the successes of those clients.

The overall page should be elegant and creative. Do not include courthouses, gavels or anything else related to the law. If you include these things, your design will automatically be excluded.
Updates

Please take note this design is now guaranteed. I look forward to receiving everyone's wonderful designs.

Target Market(s)

Persons involved in car wrecks

Industry/Entity Type

Legal

Coding

Coded - Design and coding required

Number of Pages Required

5+ page

Font styles to use
Serif
Sans Serif

Colors
ec1f27
ffffff
000000

Requirements
Must have
• Five pages which focus on representation of car wreck victims. The site must be clean and easy to navigate.
Nice to have
• Navigation bar should follow user up and down the page.
Should not have
• Gavels, court houses, anything related to the law. If your design has these aspects, it will automatically be rejected

```html
<!DOCTYPE html>
<html lang="en">
<head>
<meta charset="utf-8">
<title>FenderPals — Personal Injury Lawyers</title>
<link rel="stylesheet" href="https://fonts.googleapis.com/css2?family=Open+Sans:wght@400;600;700;800&display=swap">
<style>
:root{
  --red:#ec1f27;
  --black:#000000;
  --ink:#222222;
  --muted:#777777;
  --white:#ffffff;
  --grey-band:#e9e9e9;
  --footer:#1b1b1b;
  --footer-text:#9a9a9a;
  --rule:#dddddd;
}
*{box-sizing:border-box;margin:0;padding:0}
html,body{width:682px;height:1200px;overflow:hidden;background:var(--white)}
body{font-family:"Open Sans",Arial,sans-serif;color:var(--ink);position:relative}

/* header */
.site-header{height:64px;position:relative;text-align:center}
.brand{padding-top:12px;display:inline-flex;flex-direction:column;align-items:center}
.brand-row{display:flex;align-items:center;gap:7px}
.brand-mark{width:12px;height:12px;background:var(--red)}
.brand-name{font-weight:700;font-size:22px;color:var(--ink);line-height:28px}
.brand-tag{margin-top:2px;font-size:8px;letter-spacing:1.2px;color:var(--muted)}
.ebook-btn{position:absolute;right:60px;top:16px;background:var(--red);color:var(--white);font-size:8px;font-weight:700;padding:8px 12px;border-radius:2px}

/* nav */
.main-nav{display:flex;height:28px;margin:0 56px;background:var(--red)}
.main-nav a{color:var(--white);font-size:7px;font-weight:700;text-decoration:none;display:flex;align-items:center;justify-content:center;flex:1}
.main-nav a.active{background:var(--black);flex:0 0 80px;clip-path:polygon(0 0,100% 0,88% 100%,0 100%)}

/* hero */
.hero{position:relative;height:318px;background:linear-gradient(180deg,#9aa6ae 0%,#7f8a8f 45%,#5a6a4c 62%,#3e3f3d 100%)}
.hero-photo{position:absolute;inset:0}
.hero-copy{position:absolute;left:56px;top:102px;color:var(--white)}
.hero-title{font-size:25px;font-weight:600;letter-spacing:.5px}
.hero-text{margin-top:6px;font-size:13px;line-height:17px;width:360px}
.btn{display:inline-block;background:var(--red);color:var(--white);font-size:7px;font-weight:700;padding:6px 10px;border-radius:2px}
.hero-copy .btn{margin-top:14px}
.hero-arrow{position:absolute;top:150px}
.hero-arrow.prev{left:12px}
.hero-arrow.next{right:12px}

/* intro panels */
.intro{display:flex;height:104px}
.intro-lead{flex:0 0 410px;background:var(--red);color:var(--white);padding:18px 12px 0 56px}
.intro-lead h2{font-size:12px;font-weight:600;letter-spacing:.3px}
.intro-lead p{margin-top:8px;font-size:7px;line-height:11px;width:300px}
.intro-more{flex:1;background:var(--grey-band);padding:26px 0 0 40px}
.intro-more h2{font-size:12px;font-weight:600;color:var(--muted);border-bottom:1px solid #bbb;width:150px;padding-bottom:4px}
.intro-more .btn{margin:8px 0 0 26px;padding:6px 16px}

/* content */
.content{display:flex;padding:26px 56px 0}
.section-title{font-size:11px;font-weight:700;color:var(--ink);letter-spacing:.3px}
.work{flex:0 0 290px}
.video{margin-top:14px;height:166px;position:relative;background:linear-gradient(160deg,#6b7a6a,#3e4a44);border-radius:2px}
.video-play{position:absolute;left:50%;top:50%;width:34px;height:24px;margin:-12px 0 0 -17px;background:rgba(0,0,0,.55);border-radius:4px}
.video-play::after{content:"";position:absolute;left:14px;top:7px;border-left:9px solid var(--white);border-top:5px solid transparent;border-bottom:5px solid transparent}
.video-bar{position:absolute;left:0;right:0;bottom:0;height:14px;background:rgba(0,0,0,.75)}
.video-bar i{position:absolute;left:26px;top:6px;width:200px;height:2px;background:#666}
.video-bar b{position:absolute;left:26px;top:6px;width:40px;height:2px;background:var(--red)}
.news{margin-left:24px;flex:1}
.news-item{display:flex;margin-top:16px;padding-bottom:14px;border-bottom:1px solid var(--rule)}
.news-thumb{flex:0 0 60px;height:52px;background:linear-gradient(135deg,#b7c0c8,#6d7c8c)}
.news-body{margin-left:10px}
.news-body h3{font-size:7px;font-weight:700}
.news-date{font-size:6px;color:var(--red);margin-top:2px}
.news-body p{font-size:6px;line-height:9px;color:var(--muted);margin-top:4px}

/* testimonials */
.testimonials{padding:60px 56px 0}
.quotes{display:grid;grid-template-columns:1fr 1fr;column-gap:60px;row-gap:30px;margin-top:22px;padding:0 8px}
.quote{display:flex}
.avatar{flex:0 0 42px;height:42px;border-radius:50%;background:linear-gradient(135deg,#c9b9a6,#7a6a5a);position:relative}
.avatar::after{content:"“";position:absolute;right:-2px;top:-4px;width:14px;height:14px;border-radius:50%;background:var(--red);color:var(--white);font-size:12px;line-height:16px;text-align:center;font-weight:700}
.quote-body{margin-left:12px}
.quote-body h3{font-size:8px;font-weight:700;margin-top:4px}
.quote-body p{font-size:6px;line-height:9px;color:var(--muted);margin-top:5px;width:180px}

/* footer */
.site-footer{position:absolute;left:0;top:1033px;width:682px;height:137px;background:var(--footer);display:flex;padding:14px 56px 0;color:var(--footer-text)}
.footer-col h4{font-size:7px;font-weight:700;color:var(--white);margin-bottom:8px}
.footer-col li{list-style:none;font-size:6px;line-height:11px}
.col-nav{flex:0 0 150px}
.col-help{flex:0 0 165px}
.col-news{flex:0 0 175px}
.contact-line{display:flex;align-items:center;gap:5px;font-size:6px;line-height:12px}
.field{width:110px;height:13px;background:var(--white);color:#999;font-size:5.5px;padding:3px 4px;margin-bottom:5px}
.submit{display:inline-block;background:var(--red);color:var(--white);font-size:6px;font-weight:700;padding:3px 12px}
.social{display:flex;gap:4px}
.social span{width:14px;height:14px;border-radius:2px}
.copyright{position:absolute;left:0;top:1170px;width:682px;height:30px;background:var(--red);color:var(--white);font-size:6px;text-align:center;line-height:30px}
</style>
</head>
<body>

<header class="site-header">
  <div class="brand">
    <div class="brand-row"><span class="brand-mark"></span><span class="brand-name">FenderPals</span></div>
    <div class="brand-tag">PERSONAL INJURY LAWYERS</div>
  </div>
  <span class="ebook-btn">FREE EBOOK</span>
</header>

<nav class="main-nav">
  <a class="active">HOME</a>
  <a>CLIENT RESOURCES</a>
  <a>EXPERTISE / CAR WRECKS</a>
  <a>CONTACT US</a>
  <a>NEWS</a>
</nav>

<section class="hero">
  <div class="hero-photo" role="img" aria-label="Wrecked silver sedan on a roadside after a collision"></div>
  <div class="hero-copy">
    <h1 class="hero-title">PERSONAL INJURY LAWYERS</h1>
    <p class="hero-text">Lorem ipsum dolor sit amet, ne vel mandamus consectetuer necessitatibus. Cum veli repriminques</p>
    <span class="btn">READ MORE ›</span>
  </div>
  <svg class="hero-arrow prev" width="10" height="18" viewBox="0 0 10 18"><path d="M8 2 2 9l6 7" fill="none" stroke="#fff" stroke-width="2"/></svg>
  <svg class="hero-arrow next" width="10" height="18" viewBox="0 0 10 18"><path d="m2 2 6 7-6 7" fill="none" stroke="#fff" stroke-width="2"/></svg>
</section>

<section class="intro">
  <div class="intro-lead">
    <h2>WE ARE THE PERSONAL INJURY LAWYERS</h2>
    <p>We focus on one thing only: car wrecks. Our team stands with victims from the first call to the final settlement.</p>
  </div>
  <div class="intro-more">
    <h2>MORE ABOUT US</h2>
    <span class="btn">CLICK HERE</span>
  </div>
</section>

<section class="content">
  <div class="work">
    <h2 class="section-title">OUR WORK PROCESS</h2>
    <div class="video" role="img" aria-label="Video still of a lawyer inspecting a damaged car">
      <span class="video-play"></span>
      <span class="video-bar"><i></i><b></b></span>
    </div>
  </div>
  <div class="news">
    <h2 class="section-title">RECENT NEWS</h2>
    <article class="news-item">
      <div class="news-thumb" role="img" aria-label="Photo of the legal team"></div>
      <div class="news-body">
        <h3>LOREM IPSUM DOLOR</h3>
        <div class="news-date">June 4, 2015</div>
        <p>A client hurt in a highway collision recovered full costs after a long insurance dispute.</p>
      </div>
    </article>
    <article class="news-item">
      <div class="news-thumb" role="img" aria-label="Photo of a client meeting"></div>
      <div class="news-body">
        <h3>LOREM IPSUM DOLOR</h3>
        <div class="news-date">May 18, 2015</div>
        <p>Our team secured a fair settlement for a family struck by a distracted driver.</p>
      </div>
    </article>
  </div>
</section>

<section class="testimonials">
  <h2 class="section-title">TESTIMONIALS</h2>
  <div class="quotes">
    <div class="quote"><div class="avatar" role="img" aria-label="Client portrait"></div><div class="quote-body"><h3>QUISQUE RUTRUM</h3><p>They handled my claim with care and kept me informed every step of the way.</p></div></div>
    <div class="quote"><div class="avatar" role="img" aria-label="Client portrait"></div><div class="quote-body"><h3>QUISQUE RUTRUM</h3><p>They handled my claim with care and kept me informed every step of the way.</p></div></div>
    <div class="quote"><div class="avatar" role="img" aria-label="Client portrait"></div><div class="quote-body"><h3>QUISQUE RUTRUM</h3><p>They handled my claim with care and kept me informed every step of the way.</p></div></div>
    <div class="quote"><div class="avatar" role="img" aria-label="Client portrait"></div><div class="quote-body"><h3>QUISQUE RUTRUM</h3><p>They handled my claim with care and kept me informed every step of the way.</p></div></div>
  </div>
</section>

<footer class="site-footer">
  <div class="footer-col col-nav">
    <h4>NAVIGATION</h4>
    <ul><li>Home</li><li>About Us</li><li>Expertise / Car Wrecks</li><li>Contact Us</li><li>News</li></ul>
  </div>
  <div class="footer-col col-help">
    <h4>QUESTIONS OR ASSISTANCE</h4>
    <div class="contact-line">Feel free to contact us at</div>
    <div class="contact-line"><svg width="7" height="7" viewBox="0 0 10 10"><path d="M2 1h2l1 2-1.3 1a6 6 0 0 0 2.3 2.3L7 5l2 1v2a1 1 0 0 1-1 1A8 8 0 0 1 1 2a1 1 0 0 1 1-1z" fill="#9a9a9a"/></svg>+1 (555) 010-2040</div>
    <div class="contact-line"><svg width="7" height="7" viewBox="0 0 10 10"><rect x="1" y="2" width="8" height="6" fill="none" stroke="#9a9a9a"/><path d="m1 2 4 3 4-3" fill="none" stroke="#9a9a9a"/></svg>info@fenderpals-example.com</div>
  </div>
  <div class="footer-col col-news">
    <h4>NEWSLETTER SIGNUP</h4>
    <div class="field">Enter your name</div>
    <div class="field">Enter your email</div>
    <span class="submit">Submit</span>
  </div>
  <div class="footer-col">
    <h4>FOLLOW US</h4>
    <div class="social"><span style="background:#e8822a"></span><span style="background:#3b5998"></span><span style="background:#2aa9e0"></span></div>
  </div>
</footer>
<div class="copyright">Copyright © 2015 www.fenderpals-example.com All Rights Reserved</div>

</body>
</html>
```